Carrier needs an Amazing Flyer

Our business is needing a corporate flyer. At the moment we transport different products, some of them clasified as hazardous, through out center and south Peru-South America. We would like the flyer to comunicate punctuality, safety and profesionalism. Our corporate colors are green (C=85,M=25,Y=55,K=10) and black. At the moment, we are developing what the flyer should say (we will upload it later), but the flyer should have 04 parts: Clients, Vehicles, Services and Routes.

The information to every part is the following:

Clients: the ones listed in our webpage (www.cargavelorumbo.pe), which you can find in the option "Clientes". We add the text of this part in uploaded files with a .doc extension.

Vehicles: the ones listed in our webpage (www.cargavelorumbo.pe), which you can find in the option "Flota". We add the text of this part in uploaded files with a .doc extension.

Services: the ones listed in our webpage (www.cargavelorumbo.pe), which you can find in the option "Servicios". We add the text of this part in uploaded files with a .doc extension. The smart art is only a example. We would like too see more ideas but use the smart art as an example.

Routes: At the moment we are covering all South of Peru and his capital city, Lima. Thefore, we are transporting between cities around the mentioned area. An idea to show this can be a map of those Peru areas. We will like to receive more ideas about this. In order to help you draw the map, the cities adn towns that we most cover are: Lima, Pisco, Ica, Nasca, Chala, Atico, OcoƱa, Camana, Pedregal, Majes, Mollendo, Matarani, Ilo, Moquegua, Cocachacra, Tacna, Arequipa, Juliaca, Puno, Ilave, Desaguadero, Cusco, Sicuani, Chivay, Imata, Santa Lucia, Ayaviri, Puerto Maldonado, Macusani, Mazuco, Espinar. You can use google maps, to have an idea of where these cities and towns are. Any question just write us a message.

Target Market(s)

Other Business

Industry/Entity Type

Business

Requirements
Must have
• We are willing to print the flyer in a A4 format and bent it in two. Also, we will use the flyer as a digital presentation to send it to our clients by email. All the text in the flyer must be in spanish. For those who do not know the language, we will guide you. We don't want to many words in the flyer.
Nice to have
• We would like to see something that captures the attention of the reader, so he or she give it some minutes to check it out. Therefore, the parts should be strategically located.
Should not have
• Don't put in a map of South America. We are not transporting outside of Peru at the moment. This might give a wrong impression to new customers.

```html
<!DOCTYPE html>
<html lang="es">
<head>
<meta charset="utf-8">
<title>Folleto corporativo – Clientes, Flota y Servicios</title>
<link rel="stylesheet" href="https://fonts.googleapis.com/css2?family=Open+Sans:wght@300;400&display=swap">
<style>
  :root {
    --page-bg: #e9e6e1;
    --brand-teal: #06846f;
    --text-light: #ffffff;
    --photo-shadow: rgba(0, 0, 0, 0.45);
  }
  html, body {
    margin: 0;
    padding: 0;
    width: 1200px;
    height: 1200px;
    overflow: hidden;
    background: var(--page-bg);
  }
  .flyer {
    position: absolute;
    left: 190px;
    top: 20px;
    width: 820px;
    height: 1160px;
    background: var(--brand-teal);
    overflow: hidden;
    font-family: "Open Sans", sans-serif;
    color: var(--text-light);
    box-shadow: 0 6px 18px rgba(0,0,0,0.25);
  }
  .fleet-photo {
    position: absolute;
    left: 47px;
    width: 253px;
    height: 172px;
    border-radius: 14px;
    box-shadow: 3px 3px 4px var(--photo-shadow);
  }
  .fleet-photo--dump { top: 94px; background: linear-gradient(180deg, #7ea6d6 0%, #b9c8d8 38%, #b49e84 55%, #9c8670 100%); }
  .fleet-photo--tipping { top: 312px; background: linear-gradient(180deg, #5f94d8 0%, #a9c2dd 45%, #9a7f62 62%, #7d6650 100%); }
  .fleet-photo--trailer { top: 531px; background: linear-gradient(180deg, #6f9ed8 0%, #6f8a5c 35%, #b0704f 60%, #9a5d42 100%); }

  .info-column {
    position: absolute;
    left: 346px;
    top: 88px;
    width: 435px;
  }
  .info-section { margin: 0 0 19px; }
  .info-section h2 {
    margin: 0;
    font-weight: 400;
    font-size: 21px;
    line-height: 24px;
    letter-spacing: 0.2px;
  }
  .info-section p {
    margin: 0;
    font-weight: 300;
    font-size: 15.6px;
    line-height: 18.3px;
  }
  .base-photo {
    position: absolute;
    left: 0;
    bottom: 0;
    width: 820px;
    height: 424px;
  }
</style>
</head>
<body>
  <main class="flyer">
    <div class="fleet-photo fleet-photo--dump" role="img" aria-label="Fotografía de un camión volquete con tolva verde en una cantera"></div>
    <div class="fleet-photo fleet-photo--tipping" role="img" aria-label="Fotografía de un camión volquete descargando material"></div>
    <div class="fleet-photo fleet-photo--trailer" role="img" aria-label="Fotografía de un tracto con semirremolque plataforma"></div>

    <section class="info-column">
      <div class="info-section">
        <h2>CLIENTES</h2>
        <p>Nuestra mejor carta de presentación, es la satisfacción de nuestros clientes. Contamos con experiencia ofreciendo nuestros servicios de transporte de mercaderías en general, materiales y/o residuos peligrosos u otros por todo el sur del Perú, así como también en la ciudad de Lima;en importantes proyectos mineros como Cerro Alto, Las Quebradas; alquilando unidades para el mantenimiento de carreteras en la provincia de Arequipa y Ayacucho; Transporte local de distribución de mercaderías en Arequipa, el llamado transporte capilar; entre otros.</p>
      </div>
      <div class="info-section">
        <h2>FLOTA</h2>
        <p>Es nuestra preocupación contar con unidades en excelente estado, que nos permitan realizar nuestras operaciones sin interrupciones por mantenimientos no planificados. Por tal motivo es que contamos una flota de unidades moderna. La cual describimos a continuación.</p>
      </div>
      <div class="info-section">
        <h2>SERVICIOS</h2>
        <p>La “Superación” es uno de los valores pilares de nuestra organización. Es por eso que desde nuestra fundación a la fecha venimos incrementando la cantidad de servicios que brindamos, con el objetivo de adecuarnos a las necesidades de nuestros clientes. A la fecha los servicios que brindamos son</p>
      </div>
    </section>

    <svg class="base-photo" viewBox="0 780 870 450" preserveAspectRatio="none" aria-hidden="false">
      <defs>
        <linearGradient id="band-fade" x1="0" y1="0" x2="1" y2="0">
          <stop offset="0" stop-color="#0f8f7c"/>
          <stop offset="0.55" stop-color="#f4fbfa"/>
          <stop offset="1" stop-color="#4fb0a2"/>
        </linearGradient>
        <linearGradient id="base-scene" x1="0" y1="0" x2="0" y2="1">
          <stop offset="0" stop-color="#5b8fd6"/>
          <stop offset="0.3" stop-color="#e9e9ea"/>
          <stop offset="0.55" stop-color="#a9523d"/>
          <stop offset="0.8" stop-color="#8c6a56"/>
          <stop offset="1" stop-color="#7a6352"/>
        </linearGradient>
      </defs>
      <path d="M0,920 Q435,670 870,860 L870,890 Q435,704 0,935 Z" fill="url(#band-fade)"/>
      <path d="M0,935 Q435,704 870,890 L870,1230 L0,1230 Z" fill="url(#base-scene)" role="img" aria-label="Fotografía del equipo de trabajo frente a la sede de la empresa junto a sus camiones"/>
    </svg>
  </main>
</body>
</html>
```